Brevolt custom business card design

After a business card incorporating the attached logo, I want the following

Brevolt
-Aluminium Windows & doors
-cladding
-roof access systems
-labour hire
-disabled access audits and alterations
-general carpentry

F 7, 21 wren gully road, Pakenham 3810
Ph: 5937 2418
Fax: 5937 2451
Mob: 0400 731 946
Marcus@brevoltworks.example

Target Market(s)

Construction industry

Industry/Entity Type

Business

Contact Information for Business Card

As per brief

Font styles to use
Serif
Script

```html
<!DOCTYPE html>
<html lang="en">
<head>
<meta charset="utf-8">
<title>Brevolt business card</title>
<link href="https://fonts.googleapis.com/css2?family=Open+Sans:wght@400;700&display=swap" rel="stylesheet">
<style>
  :root {
    --bg: #e9e6e1;
    --card: #ffffff;
    --band: #efefef;
    --brand: #e3261b;
    --ink: #2b2b2b;
    --icon: #3a3a3a;
  }
  * { margin: 0; padding: 0; box-sizing: border-box; }
  html, body { width: 1200px; height: 913px; overflow: hidden; }
  body {
    background: var(--bg);
    font-family: "Open Sans", Arial, sans-serif;
    color: var(--ink);
    position: relative;
  }
  .card {
    position: absolute;
    width: 540px;
    height: 310px;
    background: var(--card);
    box-shadow: 0 6px 18px rgba(0,0,0,0.15);
    overflow: hidden;
  }
  .card-front { left: 80px; top: 80px; }
  .card-back { left: 580px; top: 520px; }

  .brand-name {
    font-family: "Open Sans", Arial, sans-serif;
    font-weight: 700;
    color: var(--brand);
    font-size: 44px;
    letter-spacing: 0.5px;
    line-height: 1;
  }
  .card-front .brand-name { position: absolute; left: 60px; top: 80px; }

  .services {
    position: absolute;
    left: 80px;
    top: 150px;
    list-style: disc;
    font-size: 15px;
    line-height: 19px;
    padding-left: 16px;
  }

  .back-band {
    position: absolute;
    left: 0; right: 0; bottom: 0;
    height: 150px;
    background: linear-gradient(180deg, #f4f4f4, var(--band));
  }
  .card-back .brand-name { position: absolute; left: 46px; top: 108px; font-size: 40px; }

  .phones {
    position: absolute;
    right: 36px;
    top: 70px;
    list-style: none;
    font-weight: 700;
    font-size: 17px;
    line-height: 24px;
  }
  .address {
    position: absolute;
    left: 46px;
    bottom: 42px;
    list-style: none;
    font-size: 13px;
    line-height: 20px;
  }
  .phones li, .address li { display: flex; align-items: center; gap: 8px; }
  .icon { width: 14px; height: 14px; flex: none; }
</style>
</head>
<body>
  <section class="card card-front">
    <div class="brand-name">Brevolt</div>
    <ul class="services">
      <li>Aluminium Windows &amp; doors</li>
      <li>Cladding</li>
      <li>Roof access systems</li>
      <li>Labour hire</li>
      <li>Disabled access audits and alterations</li>
      <li>General carpentry</li>
    </ul>
  </section>

  <section class="card card-back">
    <div class="back-band"></div>
    <div class="brand-name">Brevolt</div>
    <ul class="phones">
      <li>
        <svg class="icon" viewBox="0 0 14 14"><circle cx="7" cy="7" r="7" fill="var(--icon)"/><path d="M4.5 3.5l1.5 0 .7 2-1 .8a5 5 0 0 0 2 2l.8-1 2 .7 0 1.5c-3.5.3-6.3-2.5-6-6z" fill="#fff"/></svg>
        <span>5937 2418</span>
      </li>
      <li>
        <svg class="icon" viewBox="0 0 14 14"><circle cx="7" cy="7" r="7" fill="var(--icon)"/><rect x="5" y="3" width="4" height="8" rx="0.8" fill="#fff"/><rect x="5.8" y="4" width="2.4" height="5" fill="var(--icon)"/></svg>
        <span>0400 731 946</span>
      </li>
      <li>
        <svg class="icon" viewBox="0 0 14 14"><circle cx="7" cy="7" r="7" fill="var(--icon)"/><rect x="3.5" y="6" width="7" height="4" fill="#fff"/><rect x="5" y="3.5" width="4" height="2.5" fill="#fff"/></svg>
        <span>5937 2451</span>
      </li>
    </ul>
    <ul class="address">
      <li>
        <svg class="icon" viewBox="0 0 14 14"><circle cx="7" cy="7" r="7" fill="var(--icon)"/><path d="M7 3a2.5 2.5 0 0 1 2.5 2.5C9.5 7.5 7 11 7 11S4.5 7.5 4.5 5.5A2.5 2.5 0 0 1 7 3z" fill="#fff"/><circle cx="7" cy="5.5" r="0.9" fill="var(--icon)"/></svg>
        <span>F 7, 21 wren gully road, Pakenham 3810</span>
      </li>
      <li>
        <svg class="icon" viewBox="0 0 14 14"><circle cx="7" cy="7" r="7" fill="var(--icon)"/><rect x="3.5" y="4.5" width="7" height="5" fill="#fff"/><path d="M3.5 4.5L7 7.3l3.5-2.8" stroke="var(--icon)" stroke-width="0.8" fill="none"/></svg>
        <span>Marcus@brevoltworks.example</span>
      </li>
    </ul>
  </section>
</body>
</html>
```